Neudesign von Visitenkarten und Briefpapier für Eventmanager
Zielgruppe
Als Eventmanager bin ich seit mehr als 15 Jahren in verschiedenen Tätigkeitsfeldern und Veranstaltungsbereichen tätig.
Wechselnde Auftraggeber, Arbeitsfelder und Themen prägen meinen beruflichen Alltag.
Die Bandbreite der Tätigkeiten reicht von Organisation und Durchführung über Konzeption und Planung bis zu Management und Beratung.
Schwerpunkt und Gemeinsamkeit ist eine planerische Tätigkeit mit Umsetzung vor Ort.
Das Wort Produktionsbüro spielt in meinen Tätigkeiten immer eine große Rolle. Produktionsbüros sind die zentrale Schaltstelle bei Veranstaltungen.
Die Domain www.taktwerkstatt.de ist meine. (es gibt keinen Internetauftritt)
Bereiche: Corporate Events, Entertainment und Musik-Tourneen, Ausstellungen
international tätig
Auftraggeber sind sowohl Endkunden als auch Agenturen aus den verschiedenen Bereichen. (Eventagenturen, Tournee- und Konzertveranstalter, internationale Ausstellungsgesellschaften)
Aufgabenstellung
Entwicklung einer Wort-/Bildmarke
Stichworte: sachlich, schnörkellos, klar, nicht verspielt, zeitlos
Gestaltung von Visitenkarten und Briefpapier
Das Design muß sich ändern lassen (z.B. Umzug) und rein digital verwendbar sein – kein Druck von Briefpapier, sondern Korrespondenz lediglich digital aus MS Word/Word für MAC.
Mögliche Ansätze:
„Dornhagen“ als Personen- und Markennamen hervorheben
„stage bureau“ als überspannenden Tätigkeitsbegriff und -namen hervorheben
Das Design sollte s/w (Grautöne) oder farblich dezent sein (1 Farbe + Grau).
Im Anhang mein derzeitiges Briefpapier und die Visitenkarte. Alle diese Information sollen auch zukünftig Platz finden.

```html
<!DOCTYPE html>
<html lang="de">
<head>
<meta charset="utf-8">
<title>Dornhagen stage bureau – Briefpapier und Visitenkarte</title>
<link href="https://fonts.googleapis.com/css2?family=Questrial&display=swap" rel="stylesheet">
<style>
  :root {
    --backdrop: #e6e6e6;
    --paper: #ffffff;
    --card: #3b3b3d;
    --accent: #a9c23b;
    --ink: #2a2a2a;
    --grey: #6d6d6d;
    --light: #f2f2f2;
    --muted: #b8b8b8;
  }
  * { box-sizing: border-box; margin: 0; padding: 0; }
  html, body { width: 1200px; height: 900px; overflow: hidden; }
  body { background: var(--backdrop); position: relative; font-family: "Questrial", sans-serif; color: var(--ink); }

  /* Shared name block */
  .brand { position: absolute; display: flex; align-items: center; }
  .brand-dot { flex: none; background: var(--accent); }
  .brand-name { line-height: 1; letter-spacing: .02em; }
  .tagline { position: absolute; line-height: 1; letter-spacing: .04em; }
  .services { position: absolute; list-style: none; letter-spacing: .06em; }

  /* Letterhead */
  .letterhead {
    position: absolute; left: 40px; top: 30px; width: 594px; height: 840px;
    background: var(--paper); box-shadow: 0 2px 10px rgba(0,0,0,.12);
  }
  .letterhead .brand { left: 40px; top: 46px; gap: 12px; }
  .letterhead .brand-dot { width: 14px; height: 14px; }
  .letterhead .brand-name { font-size: 34px; color: var(--ink); }
  .letterhead .tagline { left: 66px; top: 88px; font-size: 13px; color: var(--grey); }
  .letterhead .services { right: 40px; top: 44px; text-align: right; font-size: 10px; line-height: 13px; color: var(--grey); }

  .sender-line { position: absolute; left: 40px; top: 124px; font-size: 9px; letter-spacing: .04em; color: var(--grey); }
  .recipient { position: absolute; left: 40px; top: 156px; font-size: 12px; line-height: 16px; font-style: normal; }

  .meta { position: absolute; left: 300px; top: 152px; width: 254px; font-size: 9.5px; line-height: 14px; color: var(--grey); }
  .meta-row { display: flex; justify-content: space-between; margin-bottom: 4px; }
  .meta-row dt { width: 70px; }
  .meta-row dd { text-align: right; }

  .letter-body { position: absolute; left: 40px; top: 320px; width: 470px; font-size: 11px; line-height: 15px; }
  .letter-body p { margin-bottom: 15px; }

  /* Business card */
  .business-card {
    position: absolute; left: 670px; top: 290px; width: 500px; height: 323px;
    background: var(--card); color: var(--light); box-shadow: 0 4px 14px rgba(0,0,0,.25);
  }
  .business-card .brand { left: 40px; top: 62px; gap: 18px; }
  .business-card .brand-dot { width: 22px; height: 22px; }
  .business-card .brand-name { font-size: 56px; color: var(--light); }
  .business-card .tagline { left: 80px; top: 128px; font-size: 20px; color: var(--muted); }
  .business-card .services { left: 262px; top: 192px; font-size: 13px; line-height: 19px; color: var(--light); }
</style>
</head>
<body>

<section class="letterhead" aria-label="Briefpapier">
  <div class="brand">
    <span class="brand-dot" aria-hidden="true"></span>
    <span class="brand-name">Dornhagen</span>
  </div>
  <div class="tagline">stage bureau</div>

  <ul class="services">
    <li>Konzeption</li>
    <li>Organisation</li>
    <li>Corporate Event</li>
    <li>Management</li>
    <li>Entertainment</li>
    <li>Ausstellungen</li>
  </ul>

  <div class="sender-line">Jonas Dornhagen &nbsp;|&nbsp; Ahornweg 4b &nbsp;|&nbsp; 51645 Bergheide</div>

  <address class="recipient">
    Max Mustermann<br>
    Musterstrasse 1<br>
    12345 Musterstadt
  </address>

  <dl class="meta">
    <div class="meta-row"><dt>Anschrift:</dt><dd>Jonas Dornhagen<br>Stage Bureau<br>Ahornweg 4b<br>51645 Bergheide</dd></div>
    <div class="meta-row"><dt>Telefon:<br>Telefax:</dt><dd>+49 (0) 170 555 218 40<br>+49 (0) 221 555 730 16</dd></div>
    <div class="meta-row"><dt>E-Mail:</dt><dd>dornhagen@taktwerkstatt.de</dd></div>
    <div class="meta-row"><dt>Zeichen:</dt><dd>123 456 789</dd></div>
    <div class="meta-row"><dt>Datum:</dt><dd>01.11.2013</dd></div>
  </dl>

  <div class="letter-body">
    <p>Sehr geehrte Damen und Herren,</p>
    <p>Nihil hic munitissimus contenat viri igna, non tum lentibus.<br>
    Quo usque tandem audacci psente, que muret venit.</p>
    <p>Nihil hic munitis horis hosto civilic aeciam quo et; sensi<br>
    vos quidem nostrum essis et, vid nonc fac tarbi pro vitum<br>
    tem, quam hoc teremuli senterris, vigin se num tem<br>
    acri patum cae, nostelis. Catus consenpl. Em vivit ipsi<br>
    hicere mus fac, pulis; Catuspero, pra perorem ac muli<br>
    sent quo inatur. Mor la inte iam.</p>
    <p>Ocus, quam vis inam et L. Valartu deatum Pala ve, consum<br>
    pratus, nonsus sentilina, porum porbit? Su nostrum<br>
    patus, quam potin te aciena, ure constam tem hostic<br>
    ante, videm re commorae addum diis. Ad tum fues<br>
    vitum que intrudemnos fur ingula atuus rei sedet ventisq ordum<br>
    quas, esse condam puls bonihic aeculto et ine escementrit L. con-<br>
    sulto manum us conficaper accibenirte, te, quit L. Maxim omnem<br>
    iam publiam, C. Mulego Catiorb eruncul inequi sen vit faucto vil</p>
    <p>Vivit crem publis.</p>
  </div>
</section>

<section class="business-card" aria-label="Visitenkarte">
  <div class="brand">
    <span class="brand-dot" aria-hidden="true"></span>
    <span class="brand-name">Dornhagen</span>
  </div>
  <div class="tagline">stage bureau</div>
  <ul class="services">
    <li>Konzeption</li>
    <li>Organisation</li>
    <li>Corporate Event</li>
    <li>Management</li>
    <li>Entertainment</li>
    <li>Ausstellungen</li>
  </ul>
</section>

</body>
</html>
```